Business Reporting Graph Illustration

I'm looking for a graphic design to created an illustration of a line chart I have two sample charts that I'd like elements of each combined together to create the project. Below is a link to learn more about this project. This should be designed using any product of the Adobe Suite.
Color Scheme is included within the below link. This will require 2 - 3 rounds of design before final completion.

https://www.plonvadesk.com/file/QWT8HbxuLeMRa302KD5Vpt/Graphic-Design-Project

```html
<!DOCTYPE html>
<html lang="en">
<head>
<meta charset="utf-8">
<title>Media Campaign Response Chart</title>
<link rel="stylesheet" href="https://fonts.googleapis.com/css2?family=Poppins:wght@600&display=swap">
<style>
  :root {
    --bg: #ffffff;
    --axis: #2c3e6b;
    --label: #4a6fa5;
    --icon: #4a76b0;
    --band-top: #e6ebf3;
    --band-bottom: #ffffff;
    --divider: #e2e6ee;
    --response: #f6cb7a;
    --response-fill: #fde3b0;
    --baseline: #9fb4d3;
  }
  html, body {
    margin: 0;
    padding: 0;
    width: 1200px;
    height: 1000px;
    overflow: hidden;
    background: var(--bg);
  }
  .chart { display: block; width: 1200px; height: 1000px; }
  .axis-label {
    font-family: "Poppins", sans-serif;
    font-weight: 600;
    font-size: 11px;
    fill: var(--label);
    text-anchor: middle;
  }
  .campaign-band { fill: url(#bandGradient); }
  .band-edge { stroke: var(--divider); stroke-width: 1; }
  .span-line { stroke: var(--icon); stroke-width: 1; stroke-dasharray: 5 4; opacity: .8; }
  .span-head { fill: var(--icon); }
  .axis-line, .tick { stroke: var(--axis); stroke-width: 1; }
  .response-area { fill: url(#responseGradient); stroke: none; }
  .response-line { fill: none; stroke: var(--response); stroke-width: 1.6; stroke-linejoin: round; stroke-linecap: round; }
  .baseline-line { fill: none; stroke: var(--baseline); stroke-width: 1.6; stroke-linejoin: round; }
  .tv-icon { fill: #fff; stroke: var(--icon); stroke-width: 2.5; stroke-linecap: round; }
  .radio-body { fill: var(--icon); }
  .radio-detail { stroke: #fff; stroke-width: 1.6; fill: none; stroke-linecap: round; }
</style>
</head>
<body>
<svg class="chart" viewBox="0 0 1200 1000" xmlns="http://www.w3.org/2000/svg" role="img" aria-label="Line chart of response over days 1 to 20 with two TV campaigns and one radio campaign">
  <defs>
    <linearGradient id="bandGradient" x1="0" y1="322" x2="0" y2="600" gradientUnits="userSpaceOnUse">
      <stop offset="0" stop-color="var(--band-top)"/>
      <stop offset="1" stop-color="var(--band-bottom)"/>
    </linearGradient>
    <linearGradient id="responseGradient" x1="0" y1="370" x2="0" y2="590" gradientUnits="userSpaceOnUse">
      <stop offset="0" stop-color="var(--response-fill)" stop-opacity="1"/>
      <stop offset="1" stop-color="var(--response-fill)" stop-opacity="0"/>
    </linearGradient>
  </defs>

  <!-- campaign bands -->
  <g class="campaigns">
    <rect class="campaign-band" x="103" y="322" width="248" height="364"/>
    <rect class="campaign-band" x="376" y="322" width="497" height="364"/>
    <rect class="campaign-band" x="898" y="322" width="148" height="364"/>
    <line class="band-edge" x1="103" y1="298" x2="103" y2="686"/>
    <line class="band-edge" x1="351" y1="298" x2="351" y2="686"/>
    <line class="band-edge" x1="376" y1="298" x2="376" y2="686"/>
    <line class="band-edge" x1="873" y1="298" x2="873" y2="686"/>
    <line class="band-edge" x1="898" y1="298" x2="898" y2="686"/>
    <line class="band-edge" x1="1046" y1="298" x2="1046" y2="686"/>
  </g>

  <!-- campaign spans -->
  <g class="spans">
    <line class="span-line" x1="112" y1="305" x2="342" y2="305"/>
    <polygon class="span-head" points="106,305 113,301 113,309"/>
    <polygon class="span-head" points="348,305 341,301 341,309"/>
    <line class="span-line" x1="385" y1="305" x2="864" y2="305"/>
    <polygon class="span-head" points="379,305 386,301 386,309"/>
    <polygon class="span-head" points="870,305 863,301 863,309"/>
    <line class="span-line" x1="907" y1="305" x2="1037" y2="305"/>
    <polygon class="span-head" points="901,305 908,301 908,309"/>
    <polygon class="span-head" points="1043,305 1036,301 1036,309"/>
  </g>

  <!-- TV icons -->
  <g class="tv-icon" transform="translate(227 0)">
    <line x1="-7" y1="274" x2="0" y2="280"/><line x1="7" y1="274" x2="0" y2="280"/>
    <rect x="-16" y="282" width="32" height="23" rx="3"/>
    <line x1="-9" y1="306" x2="-11" y2="309"/><line x1="9" y1="306" x2="11" y2="309"/>
  </g>
  <g class="tv-icon" transform="translate(625 0)">
    <line x1="-7" y1="274" x2="0" y2="280"/><line x1="7" y1="274" x2="0" y2="280"/>
    <rect x="-16" y="282" width="32" height="23" rx="3"/>
    <line x1="-9" y1="306" x2="-11" y2="309"/><line x1="9" y1="306" x2="11" y2="309"/>
  </g>

  <!-- radio icon -->
  <g class="radio-icon">
    <line x1="964" y1="278" x2="988" y2="287" stroke="var(--icon)" stroke-width="1.2"/>
    <rect class="radio-body" x="956" y="285" width="34" height="23" rx="3"/>
    <line class="radio-detail" x1="961" y1="291" x2="972" y2="291"/>
    <line class="radio-detail" x1="961" y1="296" x2="972" y2="296"/>
    <line class="radio-detail" x1="961" y1="301" x2="972" y2="301"/>
    <circle class="radio-detail" cx="981" cy="296" r="5"/>
  </g>

  <!-- response series -->
  <path class="response-area" d="M85 670 L115 676 L125 672 L140 672 L150 666 L160 660 L165 652 L175 648 L178 620 L180 590 L195 575 L205 530 L212 505 L220 495 L230 465 L235 462 L240 475 L245 480 L255 500 L265 512 L272 545 L275 580 L280 585 L282 605 L289 612 L292 650 L297 655 L300 673 L310 678 L320 676 L332 668 L340 666 L352 671 L370 666 L383 652 L388 625 L395 612 L408 606 L418 614 L424 612 L435 590 L442 550 L450 525 L465 515 L480 508 L488 490 L492 420 L500 380 L508 366 L515 372 L530 395 L527 420 L532 438 L545 442 L565 446 L572 470 L580 490 L595 502 L615 508 L628 520 L645 528 L665 535 L680 555 L692 580 L710 588 L730 600 L755 608 L768 614 L780 640 L800 652 L840 662 L876 665 L890 650 L905 640 L910 600 L920 585 L930 575 L935 545 L945 512 L950 508 L955 512 L965 545 L975 590 L982 610 L990 625 L995 640 L1005 646 L1015 650 L1022 660 L1035 658 L1055 652 L1062 660 L1075 665 L1105 662 L1105 686 L85 686 Z"/>
  <path class="response-line" d="M85 670 L115 676 L125 672 L140 672 L150 666 L160 660 L165 652 L175 648 L178 620 L180 590 L195 575 L205 530 L212 505 L220 495 L230 465 L235 462 L240 475 L245 480 L255 500 L265 512 L272 545 L275 580 L280 585 L282 605 L289 612 L292 650 L297 655 L300 673 L310 678 L320 676 L332 668 L340 666 L352 671 L370 666 L383 652 L388 625 L395 612 L408 606 L418 614 L424 612 L435 590 L442 550 L450 525 L465 515 L480 508 L488 490 L492 420 L500 380 L508 366 L515 372 L530 395 L527 420 L532 438 L545 442 L565 446 L572 470 L580 490 L595 502 L615 508 L628 520 L645 528 L665 535 L680 555 L692 580 L710 588 L730 600 L755 608 L768 614 L780 640 L800 652 L840 662 L876 665 L890 650 L905 640 L910 600 L920 585 L930 575 L935 545 L945 512 L950 508 L955 512 L965 545 L975 590 L982 610 L990 625 L995 640 L1005 646 L1015 650 L1022 660 L1035 658 L1055 652 L1062 660 L1075 665 L1105 662"/>

  <!-- baseline series -->
  <path class="baseline-line" d="M150 666 L230 674 L270 669 L305 677 L360 671 L430 674 L462 670 L480 675 L500 673 L550 665 L560 667 L575 663 L590 666 L605 659 L620 662 L628 673 L660 673 L670 668 L700 671 L765 671 L800 665 L850 662 L885 664 L900 668 L918 676 L935 665 L960 665 L995 668 L1015 656 L1025 660"/>

  <!-- axis -->
  <g class="axis">
    <line class="axis-line" x1="54" y1="686" x2="1145" y2="686"/>
    <g class="minor-ticks">
      <line class="tick" x1="103" y1="686" x2="103" y2="698"/><line class="tick" x1="153" y1="686" x2="153" y2="698"/>
      <line class="tick" x1="203" y1="686" x2="203" y2="698"/><line class="tick" x1="252" y1="686" x2="252" y2="698"/>
      <line class="tick" x1="302" y1="686" x2="302" y2="698"/><line class="tick" x1="351" y1="686" x2="351" y2="698"/>
      <line class="tick" x1="401" y1="686" x2="401" y2="698"/><line class="tick" x1="451" y1="686" x2="451" y2="698"/>
      <line class="tick" x1="500" y1="686" x2="500" y2="698"/><line class="tick" x1="550" y1="686" x2="550" y2="698"/>
      <line class="tick" x1="600" y1="686" x2="600" y2="698"/><line class="tick" x1="649" y1="686" x2="649" y2="698"/>
      <line class="tick" x1="699" y1="686" x2="699" y2="698"/><line class="tick" x1="749" y1="686" x2="749" y2="698"/>
      <line class="tick" x1="798" y1="686" x2="798" y2="698"/><line class="tick" x1="848" y1="686" x2="848" y2="698"/>
      <line class="tick" x1="898" y1="686" x2="898" y2="698"/><line class="tick" x1="947" y1="686" x2="947" y2="698"/>
      <line class="tick" x1="997" y1="686" x2="997" y2="698"/><line class="tick" x1="1047" y1="686" x2="1047" y2="698"/>
      <line class="tick" x1="1097" y1="686" x2="1097" y2="698"/>
    </g>
    <g class="major-ticks">
      <line class="tick" x1="128" y1="686" x2="128" y2="708"/><line class="tick" x1="178" y1="686" x2="178" y2="708"/>
      <line class="tick" x1="227" y1="686" x2="227" y2="708"/><line class="tick" x1="277" y1="686" x2="277" y2="708"/>
      <line class="tick" x1="327" y1="686" x2="327" y2="708"/><line class="tick" x1="376" y1="686" x2="376" y2="708"/>
      <line class="tick" x1="426" y1="686" x2="426" y2="708"/><line class="tick" x1="475" y1="686" x2="475" y2="708"/>
      <line class="tick" x1="525" y1="686" x2="525" y2="708"/><line class="tick" x1="575" y1="686" x2="575" y2="708"/>
      <line class="tick" x1="624" y1="686" x2="624" y2="708"/><line class="tick" x1="674" y1="686" x2="674" y2="708"/>
      <line class="tick" x1="724" y1="686" x2="724" y2="708"/><line class="tick" x1="773" y1="686" x2="773" y2="708"/>
      <line class="tick" x1="823" y1="686" x2="823" y2="708"/><line class="tick" x1="873" y1="686" x2="873" y2="708"/>
      <line class="tick" x1="922" y1="686" x2="922" y2="708"/><line class="tick" x1="972" y1="686" x2="972" y2="708"/>
      <line class="tick" x1="1022" y1="686" x2="1022" y2="708"/><line class="tick" x1="1072" y1="686" x2="1072" y2="708"/>
    </g>
    <g class="axis-labels">
      <text class="axis-label" x="128" y="727">1</text><text class="axis-label" x="178" y="727">2</text>
      <text class="axis-label" x="227" y="727">3</text><text class="axis-label" x="277" y="727">4</text>
      <text class="axis-label" x="327" y="727">5</text><text class="axis-label" x="376" y="727">6</text>
      <text class="axis-label" x="426" y="727">7</text><text class="axis-label" x="475" y="727">8</text>
      <text class="axis-label" x="525" y="727">9</text><text class="axis-label" x="575" y="727">10</text>
      <text class="axis-label" x="624" y="727">11</text><text class="axis-label" x="674" y="727">12</text>
      <text class="axis-label" x="724" y="727">13</text><text class="axis-label" x="773" y="727">14</text>
      <text class="axis-label" x="823" y="727">15</text><text class="axis-label" x="873" y="727">16</text>
      <text class="axis-label" x="922" y="727">17</text><text class="axis-label" x="972" y="727">18</text>
      <text class="axis-label" x="1022" y="727">19</text><text class="axis-label" x="1072" y="727">20</text>
    </g>
  </g>
</svg>
</body>
</html>
```